Velandre Jewellery Display Card

We are a jewellery manufacturer and need artwork for an A4 size strut card to advertise our new "Moonleaf Halo Charm "
In the attached files is a picture of the new pendant and artwork for our trademark "Velandre"
We also need to include the phrase " an expression of love "
as part of the artwork.
The background colour should be predominately white

Target Market(s)

This product has been designed as a gift for Mothers as it has their children names
engraved on the pendant

Industry/Entity Type

Manufacturer

Font styles to use
Serif
Script

Colors
ffffff

Requirements
Must have
• Artwork should be simple and elegant , the predominant look in Australian jewellery stores which is where these display cards will be is white, bright and elegant

```html
<!DOCTYPE html>
<html lang="en">
<head>
<meta charset="utf-8">
<title>Velandre – Moonleaf Halo Charm</title>
<link rel="stylesheet" href="https://fonts.googleapis.com/css2?family=Parisienne&family=Questrial&display=swap">
<style>
  :root {
    --paper: #ffffff;
    --ink-dark: #3b3b3d;
    --ink-grey: #a6a7aa;
    --rose: #e26f98;
    --heart-pink: #ee7fa2;
    --heart-soft: #f6b5c9;
    --silver-light: #f3f3f4;
    --silver-mid: #d3d4d7;
    --silver-dark: #9c9ea3;
  }
  * { margin: 0; padding: 0; box-sizing: border-box; }
  html, body { width: 1200px; height: 849px; overflow: hidden; background: var(--paper); }
  .card {
    position: relative;
    width: 1200px;
    height: 849px;
    background: var(--paper);
    overflow: hidden;
    font-family: "Questrial", sans-serif;
  }
  .hearts, .pendant-photo { position: absolute; inset: 0; }
  .product-title {
    position: absolute;
    right: 672px;
    top: 100px;
    text-align: right;
  }
  .product-title__script {
    display: block;
    font-family: "Parisienne", cursive;
    font-size: 62px;
    line-height: 1;
    color: var(--ink-dark);
  }
  .product-title__caps {
    display: block;
    margin-top: 4px;
    font-family: "Questrial", sans-serif;
    font-size: 56px;
    line-height: 1;
    color: var(--ink-dark);
    letter-spacing: 1px;
  }
  .tagline {
    position: absolute;
    left: 86px;
    top: 378px;
    color: var(--ink-grey);
    font-size: 62px;
    line-height: 1;
  }
  .tagline__line { display: block; }
  .tagline__line--second {
    margin-left: 130px;
    margin-top: 22px;
  }
  .tagline__love {
    font-family: "Parisienne", cursive;
    color: var(--rose);
    font-size: 104px;
    margin-left: 26px;
    vertical-align: -6px;
  }
  .brand-name {
    position: absolute;
    left: 652px;
    top: 726px;
    font-family: "Questrial", sans-serif;
    font-size: 80px;
    line-height: 1;
    letter-spacing: 3px;
    color: var(--ink-grey);
  }
</style>
</head>
<body>
<main class="card">
  <svg class="hearts" width="1200" height="849" viewBox="0 0 1200 849" aria-hidden="false">
    <defs>
      <radialGradient id="heart-glow" cx="50%" cy="50%" r="50%">
        <stop offset="0%" stop-color="var(--heart-pink)" stop-opacity="0.85"/>
        <stop offset="70%" stop-color="var(--heart-soft)" stop-opacity="0.5"/>
        <stop offset="100%" stop-color="var(--heart-soft)" stop-opacity="0"/>
      </radialGradient>
    </defs>
    <g role="img" aria-label="Scattered pink folded-paper hearts">
      <circle cx="224" cy="64" r="92" fill="url(#heart-glow)"/>
      <circle cx="56" cy="250" r="82" fill="url(#heart-glow)"/>
      <circle cx="102" cy="520" r="72" fill="url(#heart-glow)"/>
      <circle cx="228" cy="698" r="66" fill="url(#heart-glow)"/>
      <circle cx="64" cy="802" r="60" fill="url(#heart-glow)"/>
      <circle cx="992" cy="80" r="76" fill="url(#heart-glow)"/>
      <circle cx="1146" cy="160" r="76" fill="url(#heart-glow)"/>
      <circle cx="1128" cy="642" r="82" fill="url(#heart-glow)"/>
      <circle cx="1104" cy="806" r="72" fill="url(#heart-glow)"/>
    </g>
  </svg>

  <svg class="pendant-photo" width="1200" height="849" viewBox="0 0 1200 849">
    <defs>
      <radialGradient id="silver-sheen" cx="45%" cy="40%" r="60%">
        <stop offset="0%" stop-color="var(--silver-light)"/>
        <stop offset="75%" stop-color="var(--silver-mid)"/>
        <stop offset="100%" stop-color="var(--silver-dark)"/>
      </radialGradient>
    </defs>
    <g role="img" aria-label="Photograph of the silver Moonleaf Halo Charm: nested teardrop rings engraved with children's names around a tree-of-life centre, hung from a stone-set bail">
      <rect x="856" y="52" width="32" height="120" rx="6" fill="url(#silver-sheen)"/>
      <ellipse cx="872" cy="424" rx="240" ry="244" fill="url(#silver-sheen)"/>
    </g>
  </svg>

  <h1 class="product-title">
    <span class="product-title__script">Moonleaf Halo</span>
    <span class="product-title__caps">CHARM</span>
  </h1>

  <p class="tagline">
    <span class="tagline__line">AN EXPRESSION</span>
    <span class="tagline__line tagline__line--second">OF<span class="tagline__love">love</span></span>
  </p>

  <p class="brand-name">VELANDRE</p>
</main>
</body>
</html>
```